Mexican construction company needs a business card design

We need a business card design for a company based in Monterrey, Mexico called:

Desarrollos Quilbeta S.A. de C.V.

The company is in the construction business and I would like the businees card to be simple and concise. Please use white background and blue or black text color that say:

"Proyectos de Construcción"-- (Brief description of business)
" Rodrigo Velun Osorio"--- (My name)
"rvelun@correoplat.mx"-- (My email)
"C: (81) 52 19 67 43"-- (My cell)
"O: (81) 56 72 18 94"-- (Office phone)

Please use only the colors of my company that are attached

Please make the back of the business card blue (same blue from logo) and use the logo.

Thanks!

```html
<!DOCTYPE html>
<html lang="es">
<head>
<meta charset="utf-8">
<title>Desarrollos Quilbeta – Tarjeta de presentación</title>
<link rel="stylesheet" href="https://fonts.googleapis.com/css2?family=Michroma&family=Exo+2:wght@500;600&display=swap">
<style>
  :root {
    --navy: #14145e;
    --grey: #9ea3aa;
    --white: #ffffff;
    --backdrop: #e9eaed;
  }
  * { box-sizing: border-box; margin: 0; padding: 0; }
  html, body { width: 1200px; height: 1000px; overflow: hidden; background: var(--backdrop); }
  .canvas { position: relative; width: 1200px; height: 1000px; }

  .card {
    position: absolute;
    left: 250px;
    width: 700px;
    height: 400px;
    overflow: hidden;
    box-shadow: 0 6px 18px rgba(20, 20, 60, 0.18);
  }
  .card--front { top: 70px; background: var(--white); }
  .card--back { top: 530px; background: var(--white); }

  /* Front bands */
  .front-stripe { position: absolute; left: 0; right: 0; top: 318px; height: 12px; background: var(--grey); }
  .front-band { position: absolute; left: 0; right: 0; top: 340px; bottom: 0; background: var(--navy); }

  /* Back bands */
  .back-field { position: absolute; left: 0; right: 0; top: 0; height: 336px; background: var(--navy); }
  .back-stripe { position: absolute; left: 0; right: 0; top: 344px; height: 10px; background: var(--grey); }

  /* Brand name */
  .brand { position: absolute; display: flex; align-items: center; gap: 18px; }
  .brand__mark { width: 46px; height: 46px; background: var(--grey); flex: none; }
  .brand__name { font-family: "Michroma", sans-serif; font-weight: 400; line-height: 1.05; text-transform: uppercase; }
  .brand__small { display: block; font-size: 15px; letter-spacing: 2px; }
  .brand__large { display: block; font-size: 34px; letter-spacing: 1px; }

  .card--front .brand { left: 130px; top: 52px; }
  .card--front .brand__name { color: var(--navy); }
  .card--back .brand { left: 190px; top: 118px; }
  .card--back .brand__name { color: var(--white); }
  .card--back .brand__large { font-size: 44px; }
  .card--back .brand__small { font-size: 19px; }

  /* Front details */
  .details { position: absolute; left: 194px; top: 148px; font-family: "Exo 2", sans-serif; }
  .details__service { font-size: 15px; letter-spacing: 2px; color: var(--grey); text-transform: uppercase; font-weight: 500; }
  .details__person { margin-top: 4px; font-size: 21px; letter-spacing: 1.5px; color: var(--navy); text-transform: uppercase; font-weight: 600; }
  .contact { list-style: none; margin-top: 10px; }
  .contact__item { display: flex; align-items: center; gap: 10px; font-size: 19px; letter-spacing: 1.5px; color: var(--navy); font-weight: 600; line-height: 30px; text-transform: uppercase; }
  .contact__icon { width: 20px; height: 20px; flex: none; }
</style>
</head>
<body>
<main class="canvas">

  <section class="card card--front" aria-label="Frente de la tarjeta">
    <div class="brand">
      <span class="brand__mark"></span>
      <span class="brand__name">
        <span class="brand__small">Desarrollos</span>
        <span class="brand__large">Quilbeta</span>
      </span>
    </div>

    <div class="details">
      <p class="details__service">Proyectos de Construcción</p>
      <p class="details__person">Rodrigo Velun Osorio</p>
      <ul class="contact">
        <li class="contact__item">
          <svg class="contact__icon" viewBox="0 0 20 20" aria-hidden="true">
            <rect x="1" y="1" width="18" height="18" rx="4" fill="none" stroke="#9ea3aa" stroke-width="2"/>
            <path d="M5 7l5 4 5-4" fill="none" stroke="#9ea3aa" stroke-width="2"/>
          </svg>
          <span style="text-transform:none">rvelun@correoplat.mx</span>
        </li>
        <li class="contact__item">
          <svg class="contact__icon" viewBox="0 0 20 20" aria-hidden="true">
            <rect x="1" y="1" width="18" height="18" rx="4" fill="none" stroke="#9ea3aa" stroke-width="2"/>
            <rect x="7" y="4.5" width="6" height="11" rx="1" fill="none" stroke="#9ea3aa" stroke-width="1.6"/>
          </svg>
          <span>(81) 52 19 67 43</span>
        </li>
        <li class="contact__item">
          <svg class="contact__icon" viewBox="0 0 20 20" aria-hidden="true">
            <rect x="1" y="1" width="18" height="18" rx="4" fill="none" stroke="#9ea3aa" stroke-width="2"/>
            <path d="M6.5 5.5c-1 1 0 4 2 6s5 3 6 2l-1.8-1.8-1.7 1c-1.2-.5-2.7-2-3.2-3.2l1-1.7z" fill="#9ea3aa"/>
          </svg>
          <span>(81) 56 72 18 94</span>
        </li>
      </ul>
    </div>

    <div class="front-stripe"></div>
    <div class="front-band"></div>
  </section>

  <section class="card card--back" aria-label="Reverso de la tarjeta">
    <div class="back-field"></div>
    <div class="back-stripe"></div>
    <div class="brand">
      <span class="brand__mark"></span>
      <span class="brand__name">
        <span class="brand__small">Desarrollos</span>
        <span class="brand__large">Quilbeta</span>
      </span>
    </div>
  </section>

</main>
</body>
</html>
```